Therapy Department Recruitment Flyer

Recruitment flyer similar to nursing one attached but for Occupational Therapy and Physical Therapy. Please use pictures depicting therapy services being provided to elderly population.

```html
<!DOCTYPE html>
<html lang="en">
<head>
<meta charset="utf-8">
<title>Therapy Positions – Silver Ridge Care Center</title>
<link rel="stylesheet" href="https://fonts.googleapis.com/css2?family=Roboto:wght@300;400;500&family=Roboto+Condensed:wght@400;700&display=swap">
<style>
  :root {
    --navy: #3b4558;
    --blue: #1654a5;
    --green: #33923a;
    --ink: #2e3340;
    --paper: #f6f7f8;
    --backdrop: #9a9a9a;
  }
  * { margin: 0; padding: 0; box-sizing: border-box; }
  html, body { width: 916px; height: 1200px; overflow: hidden; background: var(--backdrop); }
  .canvas { position: relative; width: 916px; height: 1200px; }
  .flyer {
    position: absolute; left: 34px; top: 0; width: 848px; height: 1200px;
    background: linear-gradient(180deg, #ffffff 0%, var(--paper) 45%, #ffffff 100%);
    overflow: hidden;
    font-family: "Roboto", Arial, sans-serif;
  }
  .flyer-shapes { position: absolute; inset: 0; width: 100%; height: 100%; }
  .abs { position: absolute; }
  .badge {
    left: 571px; top: 392px; width: 216px; height: 216px; border-radius: 50%;
    background: var(--navy); box-shadow: 0 8px 0 var(--green);
    display: flex; flex-direction: column; align-items: center; justify-content: center;
    font-family: "Roboto Condensed", Arial, sans-serif; font-weight: 700;
    color: #ffffff; font-size: 19px; line-height: 26px; text-align: center;
  }
  .headline {
    left: 62px; top: 574px; font-weight: 500; font-size: 51px; line-height: 56px;
    color: var(--blue); letter-spacing: -0.5px;
  }
  .headline-sub {
    left: 62px; top: 626px; font-weight: 300; font-size: 47px; line-height: 52px;
    color: var(--green);
  }
  .role-bar {
    left: 0; top: 683px; width: 334px; height: 69px; background: var(--green);
    padding: 9px 0 0 68px; color: #ffffff; font-size: 24px; line-height: 27px;
  }
  .seeking {
    left: 79px; top: 785px; font-family: "Roboto Condensed", Arial, sans-serif;
    font-weight: 700; font-size: 31px; line-height: 33px; color: var(--blue);
  }
  .about {
    left: 430px; top: 786px; width: 372px; font-family: "Roboto Condensed", Arial, sans-serif;
    font-size: 18.3px; line-height: 22px; color: var(--ink);
  }
  .contact-tab {
    left: 458px; top: 944px; height: 25px; padding: 1px 22px 0 8px;
    background: var(--blue); color: #ffffff; font-family: "Roboto Condensed", Arial, sans-serif;
    font-size: 17px; line-height: 24px;
    clip-path: polygon(0 0, 92% 0, 100% 100%, 0 100%);
  }
  .contact-card {
    left: 458px; top: 975px; width: 289px; height: 106px; border: 1.5px solid var(--blue);
    padding: 6px 9px; font-family: "Roboto Condensed", Arial, sans-serif;
    font-size: 17px; line-height: 22px; color: var(--ink); background: rgba(255,255,255,0.4);
  }
  .contact-name { color: var(--blue); font-weight: 700; }
  .contact-line { display: flex; align-items: center; gap: 6px; }
  .contact-line svg { width: 15px; height: 15px; flex: none; }
</style>
</head>
<body>
<div class="canvas">
  <main class="flyer">
    <svg class="flyer-shapes" viewBox="0 0 1250 1770" preserveAspectRatio="none" aria-hidden="false">
      <defs>
        <linearGradient id="heroTone" x1="0" y1="0" x2="1" y2="1">
          <stop offset="0" stop-color="#f3f5f7"/>
          <stop offset="0.55" stop-color="#dfe6ee"/>
          <stop offset="0.8" stop-color="#6e9fd8"/>
          <stop offset="1" stop-color="#eceff2"/>
        </linearGradient>
        <linearGradient id="sessionTone" x1="0" y1="0" x2="1" y2="1">
          <stop offset="0" stop-color="#eef1f4"/>
          <stop offset="0.6" stop-color="#9bb8dc"/>
          <stop offset="1" stop-color="#4f86c9"/>
        </linearGradient>
      </defs>
      <g role="img" aria-label="Photo: a physical therapist in blue scrubs bending a patient's knee during a therapy session">
        <path d="M0 0 H1250 V635 C900 740 400 760 0 580 Z" fill="url(#heroTone)"/>
      </g>
      <path class="band-top" d="M0 580 C400 760 900 740 1250 635 V655 C900 800 400 820 0 650 Z" fill="#3b4558"/>
      <path class="band-bottom" d="M0 1600 Q300 1700 600 1712 Q950 1700 1250 1628 V1770 H0 Z" fill="#3b4558"/>
      <path class="band-bottom-line" d="M0 1590 Q300 1688 600 1700 Q950 1688 1250 1615" fill="none" stroke="#33923a" stroke-width="16"/>
      <circle class="session-ring" cx="324" cy="1627" r="286" fill="#3b4558"/>
      <g role="img" aria-label="Photo: a therapist helping an elderly man with a cane walk, wheelchair in the background">
        <circle cx="318" cy="1638" r="276" fill="url(#sessionTone)"/>
      </g>
    </svg>

    <div class="abs badge">
      <span>Silver Ridge Care Center</span>
      <span>Aspen Hollow, Nevada</span>
    </div>

    <h1 class="abs headline">THERAPY POSITIONS</h1>
    <p class="abs headline-sub">Silver Ridge Care Center</p>

    <div class="abs role-bar">Physical Therapist<br>Occupational Therapist</div>

    <p class="abs seeking">We are seeking caring<br>and compassionate<br>therapist to join our team</p>

    <p class="abs about">Silver Ridge Care Center is a Skilled Nursing Facility in Aspen Hollow, At the heart of Juniper County, Aspen Hollow is a friendly, rural mountain town in Eastern Nevada that is rich with art and history, as well as an abundance of opportunities for outdoor adventure.</p>

    <div class="abs contact-tab">Recruiting Contract</div>
    <div class="abs contact-card">
      <div class="contact-name">Dana Whitfield</div>
      <div>Director of Rehab</div>
      <div class="contact-line">
        <svg viewBox="0 0 24 24"><path fill="#1654a5" d="M6.6 10.8a15.1 15.1 0 0 0 6.6 6.6l2.2-2.2c.3-.3.7-.4 1-.2 1.1.4 2.3.6 3.6.6.6 0 1 .4 1 1V20c0 .6-.4 1-1 1A17 17 0 0 1 3 4c0-.6.4-1 1-1h3.5c.6 0 1 .4 1 1 0 1.3.2 2.5.6 3.6.1.3 0 .7-.2 1z"/></svg>
        <span>555-014-2290 Ext. 210</span>
      </div>
      <div class="contact-line">
        <svg viewBox="0 0 24 24"><rect x="2" y="5" width="20" height="14" fill="#1654a5"/><path d="M2 5 L12 13 L22 5" fill="none" stroke="#ffffff" stroke-width="1.8"/></svg>
        <span>dwhitfield@silverridgecare.example</span>
      </div>
    </div>
  </main>
</div>
</body>
</html>
```